Billboard Design for Equipment Rental Business

We need a billboard design for our equipment rental business called Brevard Machinery Company. We are based in Georgia. We rent construction tools, equipment, and dumpsters. We currently have a design but feel like we could get something better. Our phone number is 912-307-5186 and our website is www.brevardmachinery-example.com

```html
<!DOCTYPE html>
<html lang="en">
<head>
<meta charset="utf-8">
<title>Brevard Machinery Company – Billboard</title>
<link rel="stylesheet" href="https://fonts.googleapis.com/css2?family=Oswald:wght@500;600;700&family=Barlow+Condensed:ital,wght@0,600;1,700&display=swap">
<style>
  :root {
    --rental-yellow: #f7c02b;
    --ink-black: #0b0b0b;
    --page-white: #ffffff;
  }
  * { margin: 0; padding: 0; box-sizing: border-box; }
  html, body {
    width: 1200px;
    height: 1121px;
    overflow: hidden;
    background: var(--page-white);
  }
  .billboard {
    position: absolute;
    left: 101px;
    top: 415px;
    width: 998px;
    height: 290px;
    background: var(--rental-yellow);
    box-shadow: 0 6px 14px rgba(0,0,0,0.28);
    overflow: hidden;
  }
  .headline-panel {
    position: absolute;
    inset: 0;
    width: 998px;
    height: 290px;
  }
  .headline-panel path { fill: var(--ink-black); }
  .headline-panel line { stroke: var(--rental-yellow); stroke-width: 1.2; }

  .brand-block {
    position: absolute;
    left: 0;
    top: 0;
    width: 300px;
    height: 290px;
    display: flex;
    flex-direction: column;
    align-items: center;
    justify-content: center;
    color: var(--ink-black);
    font-family: "Oswald", sans-serif;
    font-weight: 600;
    text-transform: uppercase;
    line-height: 1;
  }
  .brand-mark {
    width: 54px;
    height: 54px;
    border-radius: 50%;
    background: var(--ink-black);
    margin-bottom: 22px;
  }
  .brand-name { font-size: 60px; letter-spacing: 2px; }
  .brand-sub { font-size: 19px; letter-spacing: 2.4px; margin-top: 10px; }

  .offer-title {
    position: absolute;
    left: 372px;
    top: 12px;
    width: 600px;
    text-align: center;
    font-family: "Oswald", sans-serif;
    font-weight: 700;
    font-size: 88px;
    line-height: 1;
    color: var(--rental-yellow);
    letter-spacing: 0.5px;
  }
  .offer-list {
    position: absolute;
    left: 372px;
    top: 113px;
    width: 604px;
    text-align: center;
    font-family: "Barlow Condensed", sans-serif;
    font-style: italic;
    font-weight: 700;
    font-size: 50px;
    line-height: 1;
    color: var(--rental-yellow);
    text-transform: uppercase;
    white-space: nowrap;
  }
  .contact-row {
    position: absolute;
    left: 346px;
    right: 26px;
    top: 200px;
    height: 70px;
    display: flex;
    align-items: center;
    color: var(--ink-black);
    white-space: nowrap;
  }
  .contact-phone {
    font-family: "Oswald", sans-serif;
    font-weight: 600;
    font-size: 62px;
    line-height: 1;
    letter-spacing: -0.5px;
    flex: none;
  }
  .contact-divider {
    width: 4px;
    height: 46px;
    background: var(--ink-black);
    margin: 0 10px 0 12px;
    flex: none;
  }
  .contact-web {
    font-family: "Barlow Condensed", sans-serif;
    font-weight: 600;
    font-size: 17px;
    letter-spacing: 0;
    text-transform: uppercase;
    padding-top: 14px;
    flex: none;
  }
</style>
</head>
<body>
  <main class="billboard">
    <svg class="headline-panel" viewBox="0 0 998 290" aria-hidden="true">
      <path d="M299 0 L998 0 L998 183 L392 183 Q345 183 332 138 Z"/>
      <line x1="378" y1="106" x2="970" y2="106"/>
    </svg>

    <div class="brand-block">
      <div class="brand-mark"></div>
      <div class="brand-name">Brevard</div>
      <div class="brand-sub">Machinery Company</div>
    </div>

    <h1 class="offer-title">WE RENT</h1>
    <p class="offer-list">Equipment • Tools • Dumpsters</p>

    <div class="contact-row">
      <span class="contact-phone">912-307-5186</span>
      <span class="contact-divider"></span>
      <span class="contact-web">www.brevardmachinery-example.com</span>
    </div>
  </main>
</body>
</html>
```